Professional business cards for real estate development company

I need business cards for my new real estate development company. The company, "KORVA" is a real estate development, investment, and advisory firm with a focus on multifamily, office, and mixed-use projects across primary and secondary markets in the Southeast United States.

Style preference is modern

Industry/Entity Type

Real Estate Development

Contact Information for Business Card

The business cards need to include:
Name
Title
Mailing Address
Phone Number
Web Address

Logo is attached. I would like white to be the primary color with incorporation of the company colors: #232D3A and #B5A451

Font styles to use
Other font styles liked:
• Montserrat, Avenir

Requirements
Must have
• Company Logo. No need to include the company name since the name is in the logo.
Should not have
• No line type designs

```html
<!DOCTYPE html>
<html lang="en">
<head>
<meta charset="utf-8">
<title>KORVA Business Cards</title>
<link rel="stylesheet" href="https://fonts.googleapis.com/css2?family=Arimo:wght@400;700&family=Oswald:wght@500&display=swap">
<style>
  :root {
    --stage: #1a1a1a;
    --card-white: #ffffff;
    --brand-navy: #232d3a;
    --brand-gold: #b5a451;
    --divider: #b9bec5;
  }
  * { margin: 0; padding: 0; box-sizing: border-box; }
  html, body {
    width: 1200px;
    height: 900px;
    overflow: hidden;
    background: var(--stage);
  }
  .card-stack {
    position: absolute;
    left: 320px;
    top: 100px;
    width: 560px;
    display: flex;
    flex-direction: column;
    gap: 40px;
  }
  .card {
    position: relative;
    width: 560px;
    height: 320px;
    background: var(--card-white);
    box-shadow: 0 8px 22px rgba(0,0,0,0.55);
    overflow: hidden;
  }
  /* Front */
  .card-front {
    display: flex;
    align-items: center;
    justify-content: center;
    gap: 16px;
  }
  .brand-square {
    width: 34px;
    height: 34px;
    background: var(--brand-gold);
  }
  .brand-name {
    font-family: "Arimo", Arial, sans-serif;
    font-weight: 700;
    font-size: 64px;
    letter-spacing: 4px;
    color: var(--brand-navy);
    line-height: 1;
  }
  /* Back */
  .identity {
    position: absolute;
    left: 118px;
    top: 116px;
  }
  .person-name {
    font-family: "Oswald", "Arial Narrow", sans-serif;
    font-weight: 500;
    font-size: 22px;
    letter-spacing: 0.2px;
    color: var(--brand-gold);
    text-transform: uppercase;
    line-height: 1.05;
  }
  .person-title {
    font-family: "Arimo", Arial, sans-serif;
    font-size: 14px;
    color: var(--brand-navy);
    margin-top: 2px;
  }
  .divider {
    position: absolute;
    left: 292px;
    top: 118px;
    width: 1px;
    height: 54px;
    background: var(--divider);
  }
  .contact-list {
    position: absolute;
    left: 312px;
    top: 124px;
    list-style: none;
    font-family: "Arimo", Arial, sans-serif;
    font-size: 14px;
    color: var(--brand-navy);
  }
  .contact-item {
    display: flex;
    align-items: center;
    gap: 9px;
    height: 21px;
  }
  .contact-icon { width: 13px; height: 13px; flex: none; }
  .mailing-address {
    position: absolute;
    left: 118px;
    top: 236px;
    font-family: "Arimo", Arial, sans-serif;
    font-size: 14.5px;
    color: var(--brand-navy);
  }
</style>
</head>
<body>
  <main class="card-stack">
    <section class="card card-front" aria-label="Business card front">
      <span class="brand-square" aria-hidden="true"></span>
      <span class="brand-name">KORVA</span>
    </section>

    <section class="card card-back" aria-label="Business card back">
      <div class="identity">
        <p class="person-name">Daniel Mercer</p>
        <p class="person-title">Managing Director</p>
      </div>
      <span class="divider" aria-hidden="true"></span>
      <ul class="contact-list">
        <li class="contact-item">
          <svg class="contact-icon" viewBox="0 0 24 24" aria-hidden="true">
            <path fill="#b5a451" d="M6.6 10.8a15.1 15.1 0 0 0 6.6 6.6l2.2-2.2a1 1 0 0 1 1-.25 11.4 11.4 0 0 0 3.6.57 1 1 0 0 1 1 1V20a1 1 0 0 1-1 1A17 17 0 0 1 3 4a1 1 0 0 1 1-1h3.5a1 1 0 0 1 1 1c0 1.25.2 2.45.57 3.57a1 1 0 0 1-.25 1z"/>
          </svg>
          <span>044-987 654 321</span>
        </li>
        <li class="contact-item">
          <svg class="contact-icon" viewBox="0 0 24 24" aria-hidden="true">
            <g fill="none" stroke="#b5a451" stroke-width="2">
              <circle cx="12" cy="12" r="10"/>
              <ellipse cx="12" cy="12" rx="4.5" ry="10"/>
              <path d="M2 12h20M4 7h16M4 17h16"/>
            </g>
          </svg>
          <span>www.korvadev.com</span>
        </li>
      </ul>
      <p class="mailing-address">318, Harbor Lane, Savannah, 31401</p>
    </section>
  </main>
</body>
</html>
```